Carpentry Fitouts business Van half wrap

We are looking for a half wrap on our 2020Mitsubishi Express van.
Template attached, base colour to be white

Van colour is white. The 2 blue colours from logo plus black should be used in the half wrap

Our services are :
Commercial Carpentry
Interior Fitouts
Plastering
Suspended Ceilings
Windows & Doors

Rear window to have perforated one way film

Contact details on van should be PH:0491 582 306
liam@quillmarkfitouts.com.au

Industry/Entity Type

Carpentry Fitouts

Colors
0054AA
0677BA
7BADD7
CADEEF
E8F1F8
0094D4
00A9DD
6FCCEA
C7EBF8
E9F6FB

Requirements
Nice to have
• Wrap not through door handles

```html
<!DOCTYPE html>
<html lang="en">
<head>
<meta charset="utf-8">
<title>Quillmark Fitouts – Van Half Wrap</title>
<link rel="stylesheet" href="https://fonts.googleapis.com/css2?family=Antonio:wght@600&family=Exo+2:wght@600;700&display=swap">
<style>
  :root{
    --backdrop:#eef1f4;
    --van-white:#ffffff;
    --trim:#2c2e31;
    --glass:#3b424b;
    --navy:#232b70;
    --cyan:#1aa3d2;
    --rim:#c9ccd0;
    --tail:#c8242b;
    --panel-line:#d7dadd;
  }
  html,body{margin:0;padding:0;overflow:hidden;}
  body{width:1200px;height:599px;background:var(--backdrop);}
  .wrap-artwork{display:block;width:1200px;height:599px;}
  .brand-name{font-family:"Antonio",sans-serif;font-weight:600;fill:var(--navy);font-size:104px;}
  .service{font-family:"Exo 2",sans-serif;font-weight:600;font-size:11.5px;fill:var(--navy);letter-spacing:.2px;}
  .service-dot{fill:var(--cyan);}
  .phone-number{font-family:"Exo 2",sans-serif;font-weight:700;font-size:18px;fill:#fff;letter-spacing:.6px;}
  .email{font-family:"Exo 2",sans-serif;font-weight:600;font-size:10.5px;fill:var(--cyan);}
</style>
</head>
<body>
<svg class="wrap-artwork" viewBox="0 0 1200 599" xmlns="http://www.w3.org/2000/svg" aria-label="Quillmark Fitouts van half wrap, side view">
  <!-- van body -->
  <path class="van-body" fill="var(--van-white)" d="M80 455 L78 360 Q80 300 120 278 L230 235 L345 110 Q355 98 380 97 L1035 93 Q1088 95 1092 125 L1095 440 L80 455 Z"/>

  <!-- wrap graphics -->
  <polygon class="accent-panel" fill="var(--cyan)" points="653,449 1007,93 1040,93 1094,120 1095,449"/>
  <polygon class="contact-band" fill="var(--navy)" points="320,364 732,364 653,449 330,452"/>
  <rect class="rear-trim" x="830" y="250" width="215" height="14" fill="var(--trim)"/>
  <circle class="brand-circle" cx="899" cy="233" r="96" fill="var(--navy)"/>

  <!-- body panels and trims -->
  <rect class="rear-pillar" x="1040" y="93" width="55" height="350" rx="8" fill="var(--trim)"/>
  <rect class="tail-light" x="1062" y="175" width="22" height="105" rx="6" fill="var(--tail)"/>
  <path class="front-bumper" fill="var(--trim)" d="M78 362 Q76 420 80 458 L200 462 Q188 400 210 370 L180 330 Q120 330 78 362 Z"/>
  <rect class="side-skirt" x="362" y="399" width="460" height="38" rx="8" fill="var(--trim)"/>
  <path class="headlight" fill="#c4ccd4" d="M95 300 L205 250 L215 262 Q160 295 100 318 Z"/>
  <path class="side-window" fill="var(--glass)" d="M300 140 Q315 123 340 122 L535 122 L535 238 L345 245 L300 240 Z"/>
  <rect class="mirror" x="312" y="205" width="28" height="38" rx="8" fill="var(--trim)"/>
  <g class="panel-lines" stroke="var(--panel-line)" stroke-width="1.5" fill="none">
    <line x1="553" y1="100" x2="553" y2="440"/>
    <line x1="565" y1="100" x2="565" y2="440"/>
    <line x1="824" y1="100" x2="824" y2="440"/>
  </g>
  <rect class="door-handle" x="483" y="289" width="42" height="9" rx="3" fill="var(--trim)"/>
  <rect class="door-handle" x="603" y="287" width="54" height="9" rx="3" fill="var(--trim)"/>

  <!-- wheels -->
  <g class="wheel">
    <circle cx="258" cy="443" r="62" fill="#1d1e20"/>
    <circle cx="258" cy="443" r="38" fill="var(--rim)"/>
    <circle cx="258" cy="443" r="14" fill="#4a4d52"/>
  </g>
  <g class="wheel">
    <circle cx="911" cy="436" r="62" fill="#1d1e20"/>
    <circle cx="911" cy="436" r="38" fill="var(--rim)"/>
    <circle cx="911" cy="436" r="14" fill="#4a4d52"/>
  </g>

  <!-- brand name -->
  <text class="brand-name" x="592" y="218" textLength="205" lengthAdjust="spacingAndGlyphs">QUILLMARK</text>
  <text class="brand-name" x="604" y="320" textLength="158" lengthAdjust="spacingAndGlyphs">FITOUTS</text>

  <!-- services -->
  <g class="services">
    <circle class="service-dot" cx="330" cy="286" r="3.5"/><text class="service" x="337" y="290">COMMERCIAL CARPENTRY</text>
    <circle class="service-dot" cx="352" cy="301" r="3.5"/><text class="service" x="359" y="305">INTERIOR FITOUTS</text>
    <circle class="service-dot" cx="366" cy="316" r="3.5"/><text class="service" x="373" y="320">PLASTERING</text>
    <circle class="service-dot" cx="340" cy="330" r="3.5"/><text class="service" x="347" y="334">SUSPENDED CEILINGS</text>
    <circle class="service-dot" cx="346" cy="344" r="3.5"/><text class="service" x="353" y="348">WINDOWS &amp; DOORS</text>
  </g>

  <!-- contact -->
  <path class="phone-icon" fill="var(--cyan)" d="M352 384 q2-2 4 0 l3 4 q1 2-1 3 l-1 1 q2 4 6 6 l1-1 q1-2 3-1 l4 3 q2 2 0 4 l-2 2 q-4 2-11-4 q-7-7-7-12 Z"/>
  <text class="phone-number" x="370" y="398">0491 582 306</text>
  <text class="email" x="528" y="389">liam@quillmarkfitouts.com.au</text>
</svg>
</body>
</html>
```